Biotech company website design

We are looking for innovative design of our upcoming website. We are a small biotechnology company in Europe dealing with life science products and services.
Updates

Please incorporate the following top level links:
ABOUT US, PRODUCTS, SERVICES, SUPPLIERS, NEWS AND PROMOS, CONTACT US

Target Market(s)

Science people, hospitals, universities ....

Industry/Entity Type

It Company

Requirements
Must have
• Must incorporate our current logo (its color toning)

```html
<!DOCTYPE html>
<html lang="en">
<head>
<meta charset="utf-8">
<title>VerdantBioLabs – Home</title>
<link href="https://fonts.googleapis.com/css2?family=Source+Sans+3:wght@400;600;700&display=swap" rel="stylesheet">
<style>
  :root {
    --green: #6cbc1a;
    --green-light: #9ad94a;
    --green-dark: #4f9a0c;
    --black: #111111;
    --heading: #333333;
    --body-text: #9a9a9a;
    --link-text: #666666;
    --rule: #dddddd;
    --white: #ffffff;
    --dot: #d6d6d6;
  }
  * { margin: 0; padding: 0; box-sizing: border-box; }
  html, body { width: 936px; height: 1200px; overflow: hidden; background: var(--white); }
  body { position: relative; font-family: "Source Sans 3", Arial, sans-serif; color: var(--heading); }
  .abs { position: absolute; }

  /* Header */
  .brand { left: 29px; top: 44px; display: flex; align-items: center; gap: 10px; font-size: 25px; color: var(--heading); }
  .brand-mark { width: 30px; height: 30px; background: var(--green); }
  .call-us { right: 26px; top: 30px; font-size: 16px; color: var(--green); font-weight: 600; }
  .search { left: 691px; top: 64px; width: 192px; height: 24px; border: 1px solid #bbbbbb; font-size: 12px; color: #999999; padding: 3px 7px; letter-spacing: 1px; }
  .search-btn { left: 881px; top: 60px; width: 32px; height: 32px; border-radius: 50%; background: radial-gradient(circle at 40% 35%, var(--green-light), var(--green-dark)); }
  .search-btn svg { position: absolute; left: 8px; top: 8px; }

  /* Navigation */
  .main-nav { left: 0; top: 115px; width: 936px; height: 36px; background: linear-gradient(var(--green-light), var(--green) 60%, var(--green-dark)); }
  .main-nav .home { position: absolute; left: 0; top: 0; width: 107px; height: 36px; background: var(--black); }
  .nav-item { position: absolute; top: 11px; transform: translateX(-50%); color: var(--white); font-size: 13px; font-weight: 700; text-transform: uppercase; white-space: nowrap; }

  /* Hero */
  .hero { left: 0; top: 151px; width: 936px; height: 302px; }
  .hero-shadow { left: 0; top: 453px; width: 936px; height: 40px; background: linear-gradient(#ececec, var(--white)); }
  .slider-dots { right: 8px; top: 464px; display: flex; gap: 5px; }
  .slider-dots span { width: 21px; height: 21px; border-radius: 3px; background: var(--dot); color: var(--white); font-size: 12px; text-align: center; line-height: 21px; }
  .slider-dots span.active { background: var(--black); }

  /* Welcome */
  .section-title { font-size: 20px; color: var(--heading); font-weight: 400; }
  .welcome-title { left: 19px; top: 500px; }
  .photo { display: block; }
  .welcome-photo { left: 19px; top: 536px; width: 214px; height: 141px; background: linear-gradient(90deg, #aac4dc, #e6eef5 55%, #1e2430 70%, #2d3440); }
  .welcome-text { left: 248px; top: 533px; width: 672px; font-size: 12px; line-height: 17px; color: var(--body-text); }
  .welcome-text p + p { margin-top: 16px; }
  .btn-more { display: block; width: 96px; height: 27px; background: var(--black); color: var(--white); font-size: 13px; line-height: 27px; padding-left: 11px; clip-path: polygon(0 0, 88% 0, 100% 100%, 0 100%); }
  .welcome-btn { left: 249px; top: 652px; }

  .rule { left: 0; width: 936px; height: 1px; background: var(--rule); }

  /* Feature columns */
  .feature { position: absolute; top: 728px; width: 215px; }
  .feature .section-title { height: 45px; }
  .feature .photo { width: 215px; height: 142px; }
  .feature p { margin-top: 20px; padding: 0 4px; font-size: 12px; line-height: 19px; color: var(--body-text); height: 87px; }
  .feature .btn-more { margin-top: 0; }

  /* Footer */
  .footer-links { left: 17px; top: 1116px; font-size: 13px; color: var(--link-text); letter-spacing: 0.8px; }
  .footer-links span.sep { margin: 0 6px; }
  .footer-bar { left: 0; top: 1153px; width: 936px; height: 47px; background: linear-gradient(var(--green-light), var(--green) 50%, var(--green-dark)); }
  .copyright { left: 17px; top: 1168px; font-size: 12px; color: var(--black); }
  .social { right: 10px; top: 1163px; display: flex; gap: 8px; }
  .social span { width: 27px; height: 27px; border-radius: 3px; background: linear-gradient(#ffffff, #d9d9d9); border: 1px solid #bbbbbb; }
</style>
</head>
<body>

<header>
  <div class="abs brand"><span class="brand-mark"></span>VerdantBioLabs</div>
  <div class="abs call-us">CALL US : 555.014.2210</div>
  <div class="abs search">Search...</div>
  <div class="abs search-btn">
    <svg width="16" height="16" viewBox="0 0 16 16"><circle cx="6.5" cy="6.5" r="4.5" fill="none" stroke="#fff" stroke-width="2"/><line x1="10" y1="10" x2="14" y2="14" stroke="#fff" stroke-width="2.4" stroke-linecap="round"/></svg>
  </div>
</header>

<nav class="abs main-nav">
  <div class="home"></div>
  <span class="nav-item" style="left:53px">Home</span>
  <span class="nav-item" style="left:179px">About us</span>
  <span class="nav-item" style="left:303px">Products</span>
  <span class="nav-item" style="left:429px">Services</span>
  <span class="nav-item" style="left:555px">Suppliers</span>
  <span class="nav-item" style="left:715px">News and Promos</span>
  <span class="nav-item" style="left:868px">Contact us</span>
</nav>

<svg class="abs hero" viewBox="0 0 936 302" role="img" aria-label="Scientists in a laboratory beside a green DNA double helix">
  <defs>
    <linearGradient id="lab-tone" x1="0" y1="0" x2="1" y2="1">
      <stop offset="0" stop-color="#e8ecef"/>
      <stop offset="0.6" stop-color="#c9d2d8"/>
      <stop offset="1" stop-color="#8cc24a"/>
    </linearGradient>
    <linearGradient id="helix-tone" x1="0" y1="0" x2="1" y2="0">
      <stop offset="0" stop-color="#ffffff"/>
      <stop offset="0.3" stop-color="#e6f5d2"/>
      <stop offset="1" stop-color="#9ad94a"/>
    </linearGradient>
  </defs>
  <rect width="936" height="302" fill="url(#helix-tone)"/>
  <polygon points="0,0 298,0 380,302 0,302" fill="url(#lab-tone)"/>
</svg>
<div class="abs hero-shadow"></div>
<div class="abs slider-dots"><span class="active">1</span><span>2</span><span>3</span><span>4</span></div>

<section>
  <h2 class="abs section-title welcome-title">Welcome</h2>
  <div class="abs photo welcome-photo" role="img" aria-label="Businessman in a suit standing in a bright glass office"></div>
  <div class="abs welcome-text">
    <p>Cum sociis natoque penatibus et magnis dis parturient montes, nascetur ridiculus mus. Aenean commodo ligula eget dolor. Cum sociis natoque penatibus et magnis dis parturient montes, nascetur ridiculus mus. Aenean commodo ligula eget dolor. Cum sociis natoque penatibus et magnis dis parturient montes.</p>
    <p>Cum sociis natoque penatibus et magnis dis parturient montes, nascetur ridiculus mus. Aenean commodo ligula eget dolor. Cum sociis natoque penatibus et magnis dis parturient montes.</p>
  </div>
  <a class="abs btn-more welcome-btn">View More</a>
</section>

<div class="abs rule" style="top:701px"></div>

<section>
  <div class="feature" style="left:19px">
    <h2 class="section-title">Products</h2>
    <div class="photo" role="img" aria-label="Green seedling growing in a glass test tube" style="background:linear-gradient(120deg,#f4f4f4,#dcdcdc 50%,#b8c4b0)"></div>
    <p>Cum sociis natoque penatibus et magnis dis parturient montes, nascetur ridiculus mus. Aenean commodo ligula eget dolor.</p>
    <a class="btn-more">View More</a>
  </div>
  <div class="feature" style="left:248px">
    <h2 class="section-title">Services</h2>
    <div class="photo" role="img" aria-label="Researcher in a lab coat examining a plant in a greenhouse" style="background:linear-gradient(120deg,#dfe6d6,#f2f2f2 50%,#9fbf7a)"></div>
    <p>Cum sociis natoque penatibus et magnis dis parturient montes, nascetur ridiculus mus. Aenean commodo ligula eget dolor.</p>
    <a class="btn-more">View More</a>
  </div>
  <div class="feature" style="left:476px">
    <h2 class="section-title">Suppliers</h2>
    <div class="photo" role="img" aria-label="Silhouetted scientist holding up a flask of yellow liquid against a window" style="background:linear-gradient(120deg,#1f3f7a,#5b86c8 50%,#1a2d55)"></div>
    <p>Cum sociis natoque penatibus et magnis dis parturient montes, nascetur ridiculus mus. Aenean commodo ligula eget dolor.</p>
    <a class="btn-more">View More</a>
  </div>
  <div class="feature" style="left:704px">
    <h2 class="section-title">News And Promos</h2>
    <div class="photo" role="img" aria-label="Word cloud of biotechnology terms" style="background:linear-gradient(120deg,#2a3a55,#c9a23a 50%,#3a5a80)"></div>
    <p>Cum sociis natoque penatibus et magnis dis parturient montes, nascetur ridiculus mus. Aenean commodo ligula eget dolor.</p>
    <a class="btn-more">View More</a>
  </div>
</section>

<div class="abs rule" style="top:1096px"></div>

<footer>
  <div class="abs footer-links">Home<span class="sep">|</span>About us<span class="sep">|</span>Products<span class="sep">|</span>Services<span class="sep">|</span>Suppliers<span class="sep">|</span>News And Promos<span class="sep">|</span>Contact us</div>
  <div class="abs footer-bar"></div>
  <div class="abs copyright">Copyright © 2013 Verdantbiolabs.com</div>
  <div class="abs social"><span></span><span></span><span></span><span></span><span></span></div>
</footer>

</body>
</html>
```